Ecommerce website for custom sign, woodworking, and jewelry

Fully design an ecommerce website which can be loaded into my current website. Must be able to update and modify myself

```html
<!DOCTYPE html>
<html lang="en">
<head>
<meta charset="utf-8">
<title>Oakmere Creations, LLC</title>
<link href="https://fonts.googleapis.com/css2?family=Old+Standard+TT:wght@400;700&family=Open+Sans:ital,wght@0,400;0,600;0,700;1,400&display=swap" rel="stylesheet">
<style>
:root{
  --brown:#5b2e1d;
  --brown-dark:#3f1f13;
  --blush:#fce8df;
  --grey-bg:#efefef;
  --ink:#2b2b2b;
  --muted:#777;
  --footer:#0f0f0f;
  --star:#f2a20c;
  --blue:#1f78c8;
}
*{box-sizing:border-box;margin:0;padding:0}
html,body{width:1200px;height:4364px;overflow:hidden}
body{font-family:"Open Sans",sans-serif;color:var(--ink);background:#fff;position:relative}
.serif{font-family:"Old Standard TT",serif}
section,header,nav,footer,.topbar{position:absolute;left:0;width:1200px}
.abs{position:absolute}
.center{text-align:center}
h2.section-title{font-family:"Old Standard TT",serif;font-weight:700;font-size:34px;letter-spacing:1px;text-transform:uppercase;color:var(--ink)}
h2.section-title span{color:var(--brown)}
.btn{position:absolute;background:var(--brown);color:#fff;font-family:"Old Standard TT",serif;font-weight:700;font-size:17px;letter-spacing:1px;display:flex;align-items:center;justify-content:center;border-radius:4px}

/* top bar */
.topbar{top:0;height:32px;background:#e3e3e3;font-size:12.5px}
.topbar .note{left:130px;top:8px}
.topbar .phone{left:900px;top:6px;font-family:"Old Standard TT",serif;font-size:15px;display:flex;gap:6px;align-items:center}

/* header */
header{top:32px;height:92px;background:#fff}
.brand{left:130px;top:34px;font-family:"Old Standard TT",serif;font-weight:700;font-size:25px;color:var(--brown)}
.search{left:408px;top:24px;width:424px;height:48px;border:1px solid #999;border-radius:4px;overflow:hidden}
.search span{position:absolute;left:12px;top:14px;font-size:12px;color:#888}
.search .go{position:absolute;right:0;top:0;width:122px;height:100%;background:var(--brown);display:flex;align-items:center;justify-content:center}
.cart-box{left:943px;top:24px;width:48px;height:46px;border:1px solid #999;border-radius:4px;display:flex;align-items:center;justify-content:center}
.cart-label{left:1008px;top:24px;font-family:"Old Standard TT",serif;font-weight:700;font-size:15px;color:var(--brown);text-align:center;line-height:24px}

/* nav */
nav{top:124px;height:52px;background:var(--brown);display:flex;justify-content:center;align-items:center;gap:50px}
nav a{color:#fff;text-decoration:none;font-size:16px;font-weight:600}

/* hero */
.hero{top:176px;height:560px;background:linear-gradient(120deg,#4a3424 0%,#8a6543 35%,#a87f55 55%,#6e4f35 100%)}
.hero .shade{position:absolute;inset:0;background:rgba(30,18,10,.35)}
.hero h1{left:112px;top:128px;font-family:"Old Standard TT",serif;font-weight:700;font-size:44px;line-height:46px;color:#fff;letter-spacing:2px}
.hero p{left:112px;top:242px;width:560px;color:#fff;font-size:17px;line-height:26px;font-weight:600}
.hero .btn{left:112px;top:328px;width:150px;height:54px}
.dots{left:582px;top:520px;display:flex;gap:4px}
.dots i{width:9px;height:9px;border-radius:50%;background:#fff;display:block}

/* welcome */
.welcome{top:736px;height:700px;background:var(--blush)}
.welcome h2{position:absolute;top:90px;width:100%}
.welcome .lead{left:210px;top:148px;width:780px;font-weight:700;font-size:16.5px;line-height:26px}
.welcome .body{left:210px;top:208px;width:780px;color:var(--muted);font-size:15.5px;line-height:26px}
.cat{position:absolute;top:374px;width:192px;text-align:center}
.cat .ph{width:192px;height:192px;border-radius:50%}
.cat .lbl{margin-top:22px;font-family:"Old Standard TT",serif;font-weight:700;font-size:17px;letter-spacing:1px}

/* featured */
.featured{top:1436px;height:640px}
.featured h2{position:absolute;top:88px;width:100%}
.tabs{top:170px;width:100%;display:flex;justify-content:center;gap:40px;font-weight:700;font-size:16px;color:#555}
.tabs .on{color:var(--brown)}
.card{position:absolute;top:228px;width:230px;text-align:center}
.card .ph{height:288px;position:relative}
.card .overlay{position:absolute;left:0;top:0;width:100%;padding:10px;background:rgba(255,255,255,.85);font-size:10px;line-height:25px;color:#444}
.card .overlay b{font-size:10px}
.stars{color:var(--star);font-size:13px;letter-spacing:1px;margin-top:10px}
.card .name{font-family:"Old Standard TT",serif;font-weight:700;font-size:17px;letter-spacing:1px;margin-top:6px}
.card .price{font-size:13px;font-weight:600;margin-top:6px}

/* about */
.about{top:2076px;height:514px}
.about .backing{left:94px;top:72px;width:484px;height:368px;background:var(--brown-dark);border-radius:12px}
.about .ph{left:112px;top:54px;width:466px;height:366px;border-radius:8px;border:3px solid #fff;background:linear-gradient(135deg,#c69a67,#a27447 50%,#6f4a2c)}
.about h2{left:626px;top:52px;font-family:"Old Standard TT",serif;font-size:34px;color:var(--brown);font-weight:400}
.about p{left:626px;top:104px;width:460px;color:var(--muted);font-size:14.5px;line-height:25px}
.about .btn{left:626px;top:362px;width:172px;height:56px}

/* newsletter */
.newsletter{top:2590px;height:368px;background:linear-gradient(100deg,#6a3a22,#8a5535 50%,#6b3b23)}
.newsletter h2{position:absolute;top:92px;width:100%;color:#fff}
.newsletter p{left:180px;top:152px;width:840px;color:#fff;font-size:17px;line-height:26px;text-align:center;font-weight:600}
.newsletter .field{left:257px;top:216px;width:499px;height:56px;border:2px solid #fff;border-radius:4px;color:#fff;font-size:12px;padding:19px 10px}
.newsletter .btn{left:764px;top:216px;width:178px;height:56px;background:#fff;color:var(--brown)}

/* testimonials */
.testimonials{top:2958px;height:454px;background:var(--grey-bg)}
.testimonials h2{position:absolute;top:74px;width:100%;font-family:"Old Standard TT",serif;font-size:34px;font-weight:400;color:var(--brown)}
.portrait{left:203px;top:137px;width:234px;height:234px;border-radius:50%;background:radial-gradient(circle at 50% 40%,#cfc5ba,#8e8276 70%,#5f5650)}
.quote-badge{left:294px;top:344px;width:52px;height:52px;border-radius:50%;background:var(--blue);border:3px solid #fff;color:#fff;font-family:Georgia,serif;font-size:40px;font-weight:700;text-align:center;line-height:56px}
.testimonials .stars{position:absolute;left:467px;top:150px;margin:0;font-size:15px}
.testimonials blockquote{left:467px;top:184px;width:470px;font-style:italic;color:var(--muted);font-size:13.5px;line-height:25.5px}
.testimonials .who{left:467px;top:326px;font-weight:700;font-size:19px;color:#555}
.testimonials .co{left:467px;top:362px;font-size:14px;color:var(--muted)}
.arrow-l{left:88px;top:232px}
.arrow-r{left:1086px;top:232px}

/* projects */
.projects{top:3412px;height:566px}
.projects h2{position:absolute;top:88px;width:100%}
.projects .sub{left:210px;top:146px;width:780px;font-weight:600;font-size:16.5px;line-height:26px;text-align:center}
.proj{position:absolute;top:203px;width:312px;text-align:center}
.proj .ph{height:216px}
.proj .cap{position:relative;margin:-24px 18px 0;background:#fff;padding:6px 0 0;font-family:"Old Standard TT",serif;font-weight:700;font-size:17px;letter-spacing:1px;color:var(--brown)}
.proj p{font-size:13px;line-height:26px;color:var(--muted);width:240px;margin:2px auto 0}
.circ{position:absolute;top:303px;width:40px;height:40px;border-radius:50%;background:var(--brown);color:#fff;display:flex;align-items:center;justify-content:center}

/* footer */
footer{top:3978px;height:386px;background:var(--footer);color:#fff}
.f-brand{left:96px;top:74px;font-family:"Old Standard TT",serif;font-weight:700;font-size:25px;letter-spacing:1px}
.f-about{left:96px;top:124px;width:230px;font-size:13px;line-height:21px}
.socials{left:102px;top:202px;display:flex;gap:14px}
.socials i{display:block;width:36px;height:36px;border-radius:50%}
.seal{left:106px;top:256px;width:42px;height:42px;border-radius:50%;border:2px solid #fff}
.fcol{position:absolute;top:64px}
.fcol h4{font-family:"Old Standard TT",serif;font-weight:700;font-size:16px;letter-spacing:1.5px;padding-bottom:14px;position:relative}
.fcol h4::after{content:"";position:absolute;left:0;bottom:0;width:56px;height:2px;background:#fff}
.fcol ul{list-style:none;margin-top:18px;font-size:13.5px;font-weight:600;line-height:26px}
.contact-row{position:absolute;left:890px;display:flex;align-items:center;gap:18px;font-size:13.5px;font-weight:600;line-height:22px}
.contact-row .ic{width:32px;height:32px;border-radius:50%;background:#fff;display:flex;align-items:center;justify-content:center;flex:none}
.f-rule{left:88px;top:302px;width:1024px;height:1px;background:#555}
.f-copy{left:88px;top:324px;font-size:13.5px;font-weight:600}
.f-legal{left:866px;top:324px;font-size:13.5px;font-weight:600}
</style>
</head>
<body>

<div class="topbar">
  <div class="abs note">For a more unique sign, let us design a sign for you using reclaimed barn wood</div>
  <div class="abs phone">
    <svg width="14" height="14" viewBox="0 0 24 24"><path fill="#222" d="M6.6 10.8a15.1 15.1 0 0 0 6.6 6.6l2.2-2.2a1 1 0 0 1 1-.25 11.4 11.4 0 0 0 3.6.57 1 1 0 0 1 1 1V20a1 1 0 0 1-1 1A17 17 0 0 1 3 4a1 1 0 0 1 1-1h3.5a1 1 0 0 1 1 1c0 1.25.2 2.45.57 3.57a1 1 0 0 1-.25 1z"/></svg>
    (555) 214-7730
  </div>
</div>

<header>
  <div class="abs brand">Oakmere Creations, LLC</div>
  <div class="abs search">
    <span>Search</span>
    <div class="go"><svg width="18" height="18" viewBox="0 0 24 24"><circle cx="10" cy="10" r="6.5" fill="none" stroke="#fff" stroke-width="3"/><path d="M15 15l6 6" stroke="#fff" stroke-width="3" stroke-linecap="round"/></svg></div>
  </div>
  <div class="abs cart-box"><svg width="18" height="18" viewBox="0 0 24 24"><path d="M2 3h3l2.5 11h11l2-8H6.5" fill="none" stroke="#333" stroke-width="2.4"/><circle cx="9" cy="19" r="1.8" fill="#333"/><circle cx="17" cy="19" r="1.8" fill="#333"/></svg></div>
  <div class="abs cart-label">My Cart<br>00:00</div>
</header>

<nav>
  <a href="#">HOME</a><a href="#">ABOUT US</a><a href="#">SIGNS</a><a href="#">PRODUCTS</a><a href="#">PROJECTS</a><a href="#">CONTACT US</a>
</nav>

<section class="hero" role="img" aria-label="Close-up of a carved wooden farm sign being routed in the workshop">
  <div class="shade"></div>
  <h1 class="abs">QUALITY CUSTOM SIGNS<br>AND WOODCRAFTS</h1>
  <p class="abs">Lorem ipsum dolor sit amet, consectetur adipiscing elit, sed do eiusmod tempor incididunt ut magna aliqua.</p>
  <div class="btn">GET STARTED</div>
  <div class="abs dots"><i></i><i></i><i></i><i></i></div>
</section>

<section class="welcome">
  <h2 class="section-title center">Welcome to <span>Oakmere Creations, LLC</span></h2>
  <p class="abs lead center">Lorem ipsum dolor sit amet, consectetur adipiscing elit, sed do eiusmod tempor incididunt ut labore et dolore magna aliqua.</p>
  <p class="abs body center">Lorem ipsum dolor sit amet, consectetur adipiscing elit, sed do eiusmod tempor incididunt ut labore et dolore magna aliqua. Ut enim ad minim veniam, quis nostrud exercitation ullamco laboris nisi ut aliquip ex ea commodo consequat. Duis aute irure dolor in reprehenderit in voluptate velit esse cillum dolore eu fugiat nulla pariatur. Excepteur sint occaecat cupidatat non proident, sunt in culpa qui officia deserunt mollit anim id est laborum.</p>
  <div class="cat" style="left:229px"><div class="ph" role="img" aria-label="Red painted farm sign standing outdoors in the woods" style="background:radial-gradient(circle,#a33a3a 0%,#7d5a45 55%,#5a4a3a)"></div><div class="lbl">CUSTOM SIGN</div></div>
  <div class="cat" style="left:504px"><div class="ph" role="img" aria-label="Dark wooden house number plaque on light fabric" style="background:linear-gradient(180deg,#e9e2d6 0%,#e9e2d6 33%,#4a2a1a 33%,#5b3a26 66%,#e9e2d6 66%)"></div><div class="lbl">WOOD WORKING</div></div>
  <div class="cat" style="left:779px"><div class="ph" role="img" aria-label="Hands shaping a piece of jewelry at a workbench" style="background:radial-gradient(circle,#8a6a52,#5e3f2a 60%,#3a2617)"></div><div class="lbl">JEWELRY</div></div>
</section>

<section class="featured">
  <h2 class="section-title center">Our <span>Featured Products</span></h2>
  <div class="abs tabs"><span>ALL</span><span>|</span><span class="on">CUSTOM SIGN ▾</span><span>|</span><span>WOODWORKING</span><span>|</span><span>JEWELRY</span></div>
  <div class="card" style="left:120px"><div class="ph" role="img" aria-label="Carved wooden wedding sign with names and date" style="background:linear-gradient(180deg,#8a8378 0%,#8a8378 20%,#c4a883 20%,#b09070 75%,#7a6a60 75%)"></div><div class="stars">★★★★★</div><div class="name">CUSTOM SIGN</div><div class="price">$ 140.00</div></div>
  <div class="card" style="left:363px"><div class="ph" role="img" aria-label="Red and white painted farm sign" style="background:linear-gradient(180deg,#e7e2dc 0%,#c64848 45%,#a82e30 100%)"><div class="overlay"><b>LOREM IPSUM DOLOR SIT</b><br>Consectetur adipiscing<br>Sed do eiusmod tempor<br>Incididunt ut labore<br>Sed do eiusmod tempor<br>Incididunt ut labore</div></div><div class="stars">★★★★★</div><div class="name">CUSTOM SIGN</div><div class="price">$ 140.00</div></div>
  <div class="card" style="left:607px"><div class="ph" role="img" aria-label="Dark wooden house number plaque on light fabric" style="background:linear-gradient(180deg,#ebe5da 0%,#ebe5da 30%,#4e2e1d 30%,#5f3c27 68%,#ebe5da 68%)"></div><div class="stars">★★★★★</div><div class="name">CUSTOM SIGN</div><div class="price">$ 140.00</div></div>
  <div class="card" style="left:850px"><div class="ph" role="img" aria-label="Carved wooden wedding sign with names and date" style="background:linear-gradient(180deg,#8a8378 0%,#8a8378 20%,#c4a883 20%,#b09070 75%,#7a6a60 75%)"></div><div class="stars">★★★★★</div><div class="name">CUSTOM SIGN</div><div class="price">$ 140.00</div></div>
</section>

<section class="about">
  <div class="abs backing"></div>
  <div class="abs ph" role="img" aria-label="Routed wooden farm sign resting on a workbench"></div>
  <h2 class="abs">ABOUT US</h2>
  <p class="abs">Lorem ipsum dolor sit amet, consectetur adipiscing elit, sed do eiusmod tempor incididunt ut labore et dolore magna aliqua. Ut enim ad minim veniam, quis nostrud exercitation ullamco laboris nisi ut aliquip ex ea commodo consequat. Duis aute irure dolor in reprehenderit in voluptate velit esse cillum dolore eu fugiat nulla pariatur. Excepteur sint occaecat cupidatat non proident, sunt in culpa qui officia deserunt mollit anim id est laborum.Lorem ipsum dolor sit amet, consectetur adipiscing elit, sed do eiusmod tempor incididunt ut labore et dolore magna aliqua. Ut enim ad minim veniam, quis nostrud exercitation ullamco laboris nisi</p>
  <div class="btn">GET STARTED</div>
</section>

<section class="newsletter" role="img" aria-label="Woodworking tools on a workbench under a warm brown tint">
  <h2 class="section-title center">Subscribe to Newsletter</h2>
  <p class="abs">Lorem ipsum dolor sit amet, consectetur adipiscing elit, sed do eiusmod tempor incididunt ut labore et dolore magna aliqua.</p>
  <div class="abs field">Enter The Email</div>
  <div class="btn">SUBSCRIBE</div>
</section>

<section class="testimonials">
  <h2 class="center">TESTIMONIALS</h2>
  <div class="abs portrait" role="img" aria-label="Portrait photo of the customer"></div>
  <div class="abs quote-badge">”</div>
  <div class="stars">★★★★★</div>
  <blockquote class="abs">“Lorem ipsum dolor sit amet, consectetur adipiscing elit, sed do eiusmod tempor incididunt ut labore et dolore magna aliqua. Ut enim ad minim veniam, quis nostrud exercitation ullamco laboris nisi ut aliquip ex ea commodo consequat. Duis aute irure dolor in reprehenderit in voluptate velit esse cillum dolore”</blockquote>
  <div class="abs who">John Doe</div>
  <div class="abs co">Company name</div>
  <svg class="abs arrow-l" width="26" height="40" viewBox="0 0 26 40"><path d="M22 3L5 20l17 17" fill="none" stroke="#333" stroke-width="4"/></svg>
  <svg class="abs arrow-r" width="26" height="40" viewBox="0 0 26 40"><path d="M4 3l17 17L4 37" fill="none" stroke="#333" stroke-width="4"/></svg>
</section>

<section class="projects">
  <h2 class="section-title center">Our <span>Latest Projects</span></h2>
  <p class="abs sub">Lorem ipsum dolor sit amet, consectetur adipiscing elit, sed do eiusmod tempor incididunt ut labore et dolore magna aliqua.</p>
  <div class="proj" style="left:120px"><div class="ph" role="img" aria-label="Woodworker sanding a board with dust in the air" style="background:linear-gradient(135deg,#2a1c14,#8a6040 55%,#c9a37c)"></div><div class="cap">LOREM IPSUM DOLOR SIT</div><p>Lorem ipsum dolor sit amet, consect etur adipiscing elit, sed do</p></div>
  <div class="proj" style="left:444px"><div class="ph" role="img" aria-label="Hands hammering a ring on a jeweler's block" style="background:linear-gradient(135deg,#6d6660,#3d2c22 55%,#8a8680)"></div><div class="cap">LOREM IPSUM DOLOR SIT</div><p>Lorem ipsum dolor sit amet, consect etur adipiscing elit, sed do</p></div>
  <div class="proj" style="left:769px"><div class="ph" role="img" aria-label="Red painted farm sign outdoors" style="background:linear-gradient(180deg,#3f5a2e 0%,#b23a3c 25%,#a32c2e 100%)"></div><div class="cap">LOREM IPSUM DOLOR SIT</div><p>Lorem ipsum dolor sit amet, consect etur adipiscing elit, sed do</p></div>
  <div class="circ" style="left:100px"><svg width="10" height="14" viewBox="0 0 10 14"><path d="M8 1L2 7l6 6" fill="none" stroke="#fff" stroke-width="2"/></svg></div>
  <div class="circ" style="left:1064px"><svg width="10" height="14" viewBox="0 0 10 14"><path d="M2 1l6 6-6 6" fill="none" stroke="#fff" stroke-width="2"/></svg></div>
</section>

<footer>
  <div class="abs f-brand">OAKMERE CREATIONS, LLC</div>
  <p class="abs f-about">Lorem ipsum dolor sit amet, cons ectetur adipiscing elit, sed do eiu smod tempor incidi.</p>
  <div class="abs socials"><i style="background:#3b5998"></i><i style="background:#c13584"></i><i style="background:#1da1f2"></i><i style="background:#e62117"></i><i style="background:#d9304f"></i></div>
  <div class="abs seal"></div>

  <div class="fcol" style="left:483px"><h4>QUICK LINKS</h4><ul><li>Home</li><li>About Us</li><li>Signs</li><li>Products</li><li>Projects</li><li>Contact Us</li></ul></div>
  <div class="fcol" style="left:680px"><h4>IMPORTANT</h4><ul><li>My Account</li><li>Wishlist</li><li>FAQ</li><li>Customer Service</li><li>Order History</li></ul></div>
  <div class="fcol" style="left:890px"><h4>CONTACT INFO</h4></div>

  <div class="contact-row" style="top:124px"><span class="ic"><svg width="14" height="16" viewBox="0 0 24 24"><path d="M12 2a7 7 0 0 0-7 7c0 5 7 13 7 13s7-8 7-13a7 7 0 0 0-7-7zm0 9.5a2.5 2.5 0 1 1 0-5 2.5 2.5 0 0 1 0 5z" fill="#111"/></svg></span><span>PO Box 18 Marlow,<br>OH 45000</span></div>
  <div class="contact-row" style="top:186px"><span class="ic"><svg width="14" height="14" viewBox="0 0 24 24"><path fill="#111" d="M6.6 10.8a15.1 15.1 0 0 0 6.6 6.6l2.2-2.2a1 1 0 0 1 1-.25 11.4 11.4 0 0 0 3.6.57 1 1 0 0 1 1 1V20a1 1 0 0 1-1 1A17 17 0 0 1 3 4a1 1 0 0 1 1-1h3.5a1 1 0 0 1 1 1c0 1.25.2 2.45.57 3.57a1 1 0 0 1-.25 1z"/></svg></span><span>(555) 214-7730</span></div>
  <div class="contact-row" style="top:240px"><span class="ic"><svg width="14" height="12" viewBox="0 0 24 18"><path d="M1 1h22v16H1z" fill="#111"/><path d="M1 1l11 9 11-9" fill="none" stroke="#fff" stroke-width="2"/></svg></span><span>hello@oakmere-creations.com</span></div>

  <div class="abs f-rule"></div>
  <div class="abs f-copy">© Copyrights 2020 OAKMERE CREATIONS &nbsp;&nbsp;| &nbsp;&nbsp;All Rights Reserved</div>
  <div class="abs f-legal">Privacy Policy &nbsp;&nbsp;| &nbsp;&nbsp;Term &amp; condition</div>
</footer>

</body>
</html>
```